harbor glow security & electric needs a business card

Must be attractive and modern, look professional and upscale!!
We provide alarm and cameras services and 24 hour monitoring for commercial and residential clients. In addition, the owner is a master electrician that provides services to commercial and residential clients.
We also install and service automatic gates. We previously had two different businesses but decided to merge into one, thus creating Harbor Glow Security & Electric.

Target Market(s)

Commercial Business and residential customers

Industry/Entity Type

Security

Contact Information for Business Card

Front and back design with logo and services listed

Font styles to use
Sans Serif

Colors
ec1f27
0355a3
fbee3f

Requirements
Must have
• Front of card:
• Warren Kettleby-Owner
• telephone icon and then the number 936-555-0193
• Mail icon and then email address wkettleby@mailnook.example
• World Icon then website www.yourharborglowtx.example
• Location marker and then Brenford Springs, Lakeland
• We would like to have a picture of the logo at least on the front
• Also need motto on front: We're There When You're Not
• The front of the card must also say Licensed and Insured in addition to:
• License Number: K47319
• TECL: 58617
• On the Back of the Card:
• List each of these Services with check marks:
• Residential and Commercial Electrical Services
• Electric Gates
• Alarm Systems
• Alarm Monitoring
• Cameras
• ***Use separate attached logo, the business card design is just to be used as a model***
Nice to have
• It would be nice to have the logo on back of the card in addition to these words at the bottom:
• "No job too big or small, we do it all!"
Should not have
• Anything crazy!!

```html
<!DOCTYPE html>
<html lang="en">
<head>
<meta charset="utf-8">
<title>Harbor Glow Security &amp; Electric – Business Card</title>
<link href="https://fonts.googleapis.com/css2?family=Montserrat:wght@500;600;700&display=swap" rel="stylesheet">
<style>
  :root{
    --navy:#2b3671;
    --navy-deep:#222c5f;
    --red:#e41e26;
    --white:#ffffff;
    --stage:#ece9e4;
  }
  *{box-sizing:border-box;margin:0;padding:0}
  html,body{width:1200px;height:843px;overflow:hidden;background:var(--stage);font-family:"Montserrat",Arial,sans-serif}
  .card{position:absolute;top:253px;width:558px;height:317px;overflow:hidden;box-shadow:0 4px 10px rgba(0,0,0,.25)}
  .card--front{left:28px;background:var(--white)}
  .card--back{left:615px;background:var(--navy)}

  /* front */
  .front-accent{position:absolute;left:0;top:78px;width:4px;height:160px;background:var(--red)}
  .contact{position:absolute;left:21px;top:74px;color:var(--navy);font-weight:600;font-size:14px;line-height:17.3px}
  .contact__name{font-size:17px;font-weight:700;letter-spacing:.3px}
  .contact__role{color:var(--red);font-size:14px;margin-bottom:4px}
  .contact__row{display:flex;align-items:center;gap:7px}
  .contact__row svg{width:10px;height:10px;flex:none}
  .hl{color:var(--red)}
  .front-brand{position:absolute;right:22px;top:118px;width:150px;text-align:right;color:var(--red);font-weight:700;font-size:19px;line-height:24px}

  /* back */
  .camera-art{position:absolute;left:0;top:0;width:180px;height:317px}
  .back-info{position:absolute;right:24px;top:118px;text-align:right;color:var(--white);font-weight:600}
  .back-brand{font-size:15px;font-weight:700;letter-spacing:.2px}
  .motto{font-size:9.5px;font-weight:500;letter-spacing:.6px;text-transform:uppercase;margin:6px 0 9px}
  .services{list-style:none;font-size:13.3px;line-height:17.3px;margin-right:-14px}
  .services li{display:flex;justify-content:flex-end;align-items:center;gap:4px}
  .services svg{width:10px;height:10px}
  .slogan{position:absolute;right:26px;bottom:34px;color:var(--white);font-size:12.5px;font-weight:500;letter-spacing:.5px;text-transform:uppercase}
</style>
</head>
<body>

<section class="card card--front">
  <div class="front-accent"></div>
  <div class="contact">
    <div class="contact__name">Warren Kettleby</div>
    <div class="contact__role">Owner</div>
    <div class="contact__row"><svg viewBox="0 0 10 10"><path d="M2 0.5 L3.6 2.6 2.7 3.6 C3.3 5 4.6 6.5 6.2 7.3 L7.2 6.4 9.3 8 8 9.6 C4.6 9.4 0.6 5.5 0.4 1.9Z" fill="var(--red)"/></svg><span>936-555-0193</span></div>
    <div class="contact__row"><svg viewBox="0 0 10 10"><rect x="0.6" y="1.8" width="8.8" height="6.4" fill="none" stroke="var(--red)" stroke-width="1"/><path d="M0.6 1.8 5 5.4 9.4 1.8" fill="none" stroke="var(--red)" stroke-width="1"/></svg><span>wkettleby@mailnook.example</span></div>
    <div class="contact__row"><svg viewBox="0 0 10 10"><g fill="none" stroke="var(--red)" stroke-width=".9"><circle cx="5" cy="5" r="4.4"/><ellipse cx="5" cy="5" rx="1.9" ry="4.4"/><path d="M0.6 5H9.4M1.3 2.8H8.7M1.3 7.2H8.7"/></g></svg><span>www.<span class="hl">yourharborglowtx</span>.example</span></div>
    <div class="contact__row"><svg viewBox="0 0 10 10"><path d="M5 0.3C3 0.3 1.5 1.8 1.5 3.7 1.5 6.3 5 9.8 5 9.8S8.5 6.3 8.5 3.7C8.5 1.8 7 0.3 5 0.3Z" fill="var(--red)"/><circle cx="5" cy="3.7" r="1.3" fill="#fff"/></svg><span>Brenford Springs, Lakeland</span></div>
    <div>Licensed and Insured</div>
    <div>License Number: <span class="hl">K47319</span></div>
    <div>TECL: <span class="hl">58617</span></div>
  </div>
  <div class="front-brand">Harbor Glow Security &amp; Electric</div>
</section>

<section class="card card--back">
  <svg class="camera-art" viewBox="0 0 180 317" role="img" aria-label="Illustration of a red security camera on a mounting arm">
    <defs>
      <linearGradient id="camTone" x1="0" y1="0" x2="1" y2="1">
        <stop offset="0" stop-color="#ffffff"/>
        <stop offset=".45" stop-color="#e41e26"/>
        <stop offset="1" stop-color="#3b4684"/>
      </linearGradient>
    </defs>
    <path d="M0 0H150V150C150 240 90 300 0 317Z" fill="url(#camTone)"/>
  </svg>
  <div class="back-info">
    <div class="back-brand">Harbor Glow Security &amp; Electric</div>
    <div class="motto">We're there when you're not</div>
    <ul class="services">
      <li>Residential &amp; Commercial Electrical Services<svg viewBox="0 0 10 10"><path d="M1 5.5 4 8.5 9 1.5" fill="none" stroke="var(--red)" stroke-width="1.8"/></svg></li>
      <li>Electric Gates<svg viewBox="0 0 10 10"><path d="M1 5.5 4 8.5 9 1.5" fill="none" stroke="var(--red)" stroke-width="1.8"/></svg></li>
      <li>Alarm Systems<svg viewBox="0 0 10 10"><path d="M1 5.5 4 8.5 9 1.5" fill="none" stroke="var(--red)" stroke-width="1.8"/></svg></li>
      <li>Alarm Monitoring<svg viewBox="0 0 10 10"><path d="M1 5.5 4 8.5 9 1.5" fill="none" stroke="var(--red)" stroke-width="1.8"/></svg></li>
      <li>Cameras<svg viewBox="0 0 10 10"><path d="M1 5.5 4 8.5 9 1.5" fill="none" stroke="var(--red)" stroke-width="1.8"/></svg></li>
    </ul>
  </div>
  <div class="slogan">No job too big or small, we do it all</div>
</section>

</body>
</html>
```